Wine Label Design for Ferrant Estate

I need a front and back label for a new wine I am making. I am looking for a classic, elegant and serious wine label. I would like the label to be white with blue and black writing. The blue will be the distinction in the label. The color of blue will be unique and catch the eye. The font of the writing will be unique and could also serve as the brand image for Ferrant Estate. The label can have a design but should be simple and distinct. I envision the paper quality of the label to textured, high quality and add to the overall image of the label.
The label will be timeless. The price of this wine will be $85.00 a bottle, and the label should match a higher priced wine. This wine is family owned and operated.
The writing on the front and back label will be:

FRONT Label-

Ferrant Estate

Howell Mountain

Napa Valley

2022 Cabernet Sauvignon

Back Label-

Cellared and Bottled by Ferrant Estate, Cedarvale, CA 94612

GOVERNMENT WARNING: (1) According to the Surgeon General, women should not drink alcoholic beverages during pregnancy because of the risk of birth defects. (2) Consumption of alcoholic beverages impairs your ability to drive a car or operate machinery, and may cause health problems.

Alc. 14.5% by Vol.

750 ml

Contains Sulfites

```html
<!DOCTYPE html>
<html lang="en">
<head>
<meta charset="utf-8">
<title>Ferrant Estate — Front and Back Labels</title>
<link rel="stylesheet" href="https://fonts.googleapis.com/css2?family=Cinzel:wght@500&family=Josefin+Sans:wght@400;600&family=Pinyon+Script&display=swap">
<style>
  :root {
    --backdrop: #3a3a3d;
    --paper: #f3f3f1;
    --ink: #2b2b2e;
    --estate-blue: #2f2fa8;
    --emboss: #d9d9d8;
    --emboss-text: #c6c6c4;
    --frame: #3a3a3d;
  }
  * { box-sizing: border-box; margin: 0; padding: 0; }
  html, body { width: 1200px; height: 900px; overflow: hidden; }
  body {
    background: var(--backdrop);
    display: flex;
    align-items: center;
    justify-content: center;
    gap: 60px;
    font-family: "Josefin Sans", sans-serif;
    color: var(--ink);
  }
  .label {
    width: 400px;
    height: 560px;
    background: var(--paper);
    padding: 14px;
    box-shadow: 0 12px 40px rgba(0,0,0,0.35);
  }
  .label__frame {
    width: 100%;
    height: 100%;
    border: 1px solid var(--frame);
    display: flex;
    flex-direction: column;
    align-items: center;
    text-align: center;
  }
  .brand { color: var(--estate-blue); font-family: "Cinzel", serif; font-weight: 500; }
  .brand__name { font-size: 38px; letter-spacing: 0.2em; margin-left: 0.2em; line-height: 1; }
  .brand__sub { font-size: 13px; letter-spacing: 0.6em; margin-left: 0.6em; margin-top: 8px; }

  .emblem { margin: 48px 0 0; width: 140px; height: 140px; border-radius: 50%;
    border: 3px solid var(--emboss); display: flex; align-items: center; justify-content: center; }
  .emblem__name { font-family: "Cinzel", serif; font-weight: 500; font-size: 17px;
    letter-spacing: 0.18em; color: var(--emboss-text); }

  .appellation { font-size: 16px; letter-spacing: 0.08em; }
  .varietal { font-family: "Pinyon Script", cursive; font-size: 34px; line-height: 1.1; }
  .region { font-size: 15px; letter-spacing: 0.16em; }
  .vintage { font-size: 18px; font-weight: 600; letter-spacing: 0.1em; }

  .label--front .brand { margin-top: 56px; }
  .label--front .appellation { margin-top: 68px; }
  .label--front .region { margin-top: 6px; }
  .label--front .vintage { margin-top: 26px; }

  .label--back .brand { margin-top: 40px; }
  .label--back .brand__name { font-size: 30px; }
  .label--back .brand__sub { font-size: 11px; margin-top: 6px; }
  .label--back .appellation { margin-top: 22px; font-size: 13px; }
  .label--back .varietal { font-size: 28px; }
  .label--back .region { font-size: 12px; letter-spacing: 0.12em; margin-top: 4px; }
  .rule { width: 70px; height: 1px; background: var(--ink); margin: 24px 0 20px; }
  .bottler { font-size: 11px; letter-spacing: 0.08em; line-height: 1.6; text-transform: uppercase; }
  .alcohol { font-size: 12px; letter-spacing: 0.1em; margin-top: 8px; text-transform: uppercase; }
  .warning { margin-top: 22px; padding: 0 26px; font-size: 10px; line-height: 1.55;
    letter-spacing: 0.04em; text-align: justify; text-transform: uppercase; }
  .warning strong { font-weight: 600; }
  .fineprint { margin-top: auto; margin-bottom: 22px; width: 100%; padding: 0 26px;
    display: flex; justify-content: space-between; font-size: 11px; letter-spacing: 0.08em;
    text-transform: uppercase; }
</style>
</head>
<body>
  <section class="label label--front" aria-label="Front label">
    <div class="label__frame">
      <div class="brand">
        <div class="brand__name">FERRANT</div>
        <div class="brand__sub">ESTATE</div>
      </div>
      <div class="emblem"><span class="emblem__name">FERRANT</span></div>
      <div class="appellation">HOWELL MOUNTAIN</div>
      <div class="varietal">Cabernet Sauvignon</div>
      <div class="region">NAPA VALLEY</div>
      <div class="vintage">2022</div>
    </div>
  </section>

  <section class="label label--back" aria-label="Back label">
    <div class="label__frame">
      <div class="brand">
        <div class="brand__name">FERRANT</div>
        <div class="brand__sub">ESTATE</div>
      </div>
      <div class="appellation">HOWELL MOUNTAIN</div>
      <div class="varietal">Cabernet Sauvignon</div>
      <div class="region">NAPA VALLEY, 2022</div>
      <div class="rule"></div>
      <p class="bottler">Cellared and bottled by<br>Ferrant Estate, Cedarvale, CA 94612</p>
      <p class="alcohol">Alc. 14.5% by Vol.</p>
      <p class="warning"><strong>Government warning:</strong> (1) According to the Surgeon General, women should not drink alcoholic beverages during pregnancy because of the risk of birth defects. (2) Consumption of alcoholic beverages impairs your ability to drive a car or operate machinery, and may cause health problems.</p>
      <div class="fineprint"><span>750 ml</span><span>Contains sulfites</span></div>
    </div>
  </section>
</body>
</html>
```